Perfume label

For a new perfume label I need a label design and box design for a square bottle

What to include on the label
Name: Bel-Qamir, House of Mists
Fragrance description : Oudh, Roses
Fragrance number: 1
50ml
Perfume ingredient list on the box

Square bottle and Box

Label design preferences: Modern minimalistic with a little luxury touch.
Label to cover two sides of the box (wrap around) refer to drawing in attachment. Both on the box as the bottle.

```html
<!DOCTYPE html>
<html lang="en">
<head>
<meta charset="utf-8">
<title>Bel-Qamir — Perfume Label</title>
<link href="https://fonts.googleapis.com/css2?family=Marcellus&family=Montserrat:wght@400;500&display=swap" rel="stylesheet">
<style>
  :root {
    --bg: #ffffff;
    --ink: #4a4a4a;
    --ink-soft: #5c5c5c;
    --rule: #6e6e6e;
    --border: #7a7a7a;
    --accent: #e0262b;
  }
  html, body {
    margin: 0;
    padding: 0;
    width: 1200px;
    height: 1200px;
    overflow: hidden;
    background: var(--bg);
  }
  .label {
    position: absolute;
    left: 120px;
    top: 198px;
    width: 960px;
    height: 804px;
    box-sizing: border-box;
    border: 1.5px solid var(--border);
    border-radius: 18px;
    background: var(--bg);
  }
  .label > * { position: absolute; margin: 0; }
  .brand-name {
    left: 58px;
    top: 78px;
    font-family: "Marcellus", serif;
    font-size: 52px;
    font-weight: 400;
    letter-spacing: 2px;
    color: var(--ink);
    line-height: 1;
  }
  .brand-tagline {
    left: 58px;
    top: 186px;
    font-family: "Montserrat", sans-serif;
    font-size: 30px;
    font-weight: 400;
    letter-spacing: 1.5px;
    color: var(--ink);
    line-height: 1;
  }
  .rule {
    height: 0;
    border-top: 1.5px solid var(--rule);
  }
  .rule--left { left: 58px; width: 400px; }
  .rule--right { left: 486px; width: 415px; }
  .rule--top { top: 150px; }
  .rule--mid { top: 249px; }
  .rule--bottom { top: 716px; }
  .scent-notes {
    left: 58px;
    top: 288px;
    font-family: "Montserrat", sans-serif;
    font-size: 31px;
    font-weight: 400;
    letter-spacing: -0.5px;
    color: var(--accent);
    line-height: 1;
  }
  .fragrance-number {
    left: 58px;
    top: 350px;
    font-family: "Montserrat", sans-serif;
    font-size: 31px;
    font-weight: 400;
    letter-spacing: -1.2px;
    color: var(--ink-soft);
    line-height: 1;
  }
  .volume {
    left: 56px;
    top: 698px;
    font-family: "Montserrat", sans-serif;
    font-size: 45px;
    font-weight: 400;
    letter-spacing: -2px;
    color: var(--ink-soft);
    line-height: 1;
  }
  .ingredients {
    left: 486px;
    width: 420px;
    font-family: "Montserrat", sans-serif;
    font-size: 14.5px;
    line-height: 20px;
    color: var(--ink-soft);
  }
  .ingredients--first { top: 352px; }
  .ingredients--second { top: 494px; }
</style>
</head>
<body>
  <section class="label" aria-label="Bel-Qamir perfume label">
    <h1 class="brand-name">BEL-QAMIR</h1>
    <div class="rule rule--left rule--top"></div>
    <div class="rule rule--right rule--top"></div>

    <p class="brand-tagline">HOUSE OF MISTS</p>
    <div class="rule rule--left rule--mid"></div>
    <div class="rule rule--right rule--mid"></div>

    <p class="scent-notes">Oudh, Roses</p>
    <p class="fragrance-number">Fragrance number: 1</p>

    <p class="ingredients ingredients--first">Lorem ipsum dolor sit amet, consectetur adipiscing elit, sed do eiusmod tempor incididunt ut labore et dolore magna aliqua. Ut enim ad minim veniam, quis nostrud exercitation ullamco laboris nisi ut aliquip</p>
    <p class="ingredients ingredients--second">Lorem ipsum dolor sit amet, consectetur adipiscing elit, sed do eiusmod tempor incididunt ut labore et dolore magna aliqua. Ut enim ad minim veniam, quis nostrud exercitation ullamco laboris nisi ut aliquip</p>

    <p class="volume">50ml</p>
    <div class="rule rule--right rule--bottom"></div>
  </section>
</body>
</html>
```